New website for Pollard Law Firm at www.keepwinning-example.com

We are a professional law firm located in the Nashville, Tennessee USA area. We focus on personal injury law. We are looking for a slick new website that is user friendly for updating with new blogs, videos, etc. The primary colors should be red, black, and white. It should load extremely fast and have a good mobile component. The pages for the design will include a home page, about us, news, contact us, and practice page. The practice page will be copied for all the practice areas including motor vehicle accidents, slip and fall accidents, dog bites, etc. We have included an image which we would like to include in the new site which shows the color scheme The image is called banner-Car Wreck. The new website should NOT have gavels, court houses, law books, scales or the typical images for a law firm.

Target Market(s)

People in Tennessee involved in accidents

Industry/Entity Type

Legal services, law firm

Coding

Coded - Design and coding required

Number of Pages Required

5+ page

Font styles to use
Serif

Colors
EB3D1F
EC4F4E
F09395
F8D3D4
FCEDEE

Requirements
Should not have
• Gavels, columns, scales, law related images

```html
<!DOCTYPE html>
<html lang="en">
<head>
<meta charset="utf-8">
<title>News – Pollard Law Firm</title>
<link href="https://fonts.googleapis.com/css2?family=Playfair+Display:wght@400;700&family=Montserrat:wght@400;500;700;800&display=swap" rel="stylesheet">
<style>
:root{
  --red:#c42227;
  --ink:#171c24;
  --white:#ffffff;
  --text:#1f232b;
  --muted:#d9dbe0;
  --rule:#3a404a;
}
*{box-sizing:border-box;margin:0;padding:0}
html,body{width:991px;height:1200px;overflow:hidden;background:var(--white)}
body{position:relative;font-family:"Montserrat",sans-serif;color:var(--text)}
a{color:inherit;text-decoration:none}

.hero-photo{position:absolute;left:0;top:0;width:639px;height:366px;
  background:linear-gradient(120deg,#d8d4cf 0%,#8a7c70 35%,#3d3f47 60%,#6b625b 85%,#c9b9a8 100%)}
.nav-bar{position:absolute;left:542px;top:0;width:449px;height:73px;background:var(--ink)}
.hero-panel{position:absolute;left:639px;top:0;width:352px;height:327px;background:var(--ink)}

.brand{position:absolute;left:73px;top:27px;color:var(--white);
  font-family:"Playfair Display",serif;font-size:19px;font-weight:400;letter-spacing:.5px}

.main-nav{position:absolute;top:29px;left:578px;display:flex;gap:18px;font-size:11px;font-weight:500;color:var(--white)}
.call-btn{position:absolute;left:880px;top:20px;width:37px;height:34px;background:var(--red);display:flex;align-items:center;justify-content:center}

.hero-text{position:absolute;left:614px;top:113px;color:var(--white)}
.eyebrow{font-size:12px;font-weight:700;letter-spacing:2.6px}
.hero-title{margin-top:10px;font-family:"Playfair Display",serif;font-weight:700;font-size:40px;line-height:39px;letter-spacing:.5px}
.hero-title em{font-style:normal;color:var(--red)}

.post-card{position:absolute;top:430px;width:277px;height:196px;color:var(--white);text-align:center;padding:42px 18px 0}
.post-card.red{background:var(--red)}
.post-card.dark{background:var(--ink)}
.post-title{font-family:"Playfair Display",serif;font-weight:400;font-size:23px;line-height:26px;letter-spacing:.5px}
.post-meta{margin-top:10px;font-size:9.5px;font-weight:700;letter-spacing:1.8px;line-height:12.5px}

.feature-post{position:absolute;left:75px;top:632px;width:842px;height:223px;background:var(--white);
  box-shadow:0 12px 40px rgba(0,0,0,.08);text-align:center;padding-top:73px}
.feature-post .post-title{font-size:24px;color:var(--text);letter-spacing:1px}
.feature-post .post-meta{color:var(--red);margin-top:14px}

.site-footer{position:absolute;left:0;top:948px;width:991px;height:252px;background:var(--ink);color:var(--white)}
.footer-brand{position:absolute;left:75px;top:56px;font-family:"Playfair Display",serif;font-size:24px;color:var(--red);letter-spacing:.5px}
.footer-col{position:absolute;top:53px}
.footer-col h3{font-weight:800;font-size:16px;letter-spacing:-.3px;text-transform:uppercase;margin-bottom:12px}
.footer-col li{list-style:none;font-size:10px;line-height:18.5px}
.contact li{display:flex;gap:8px;align-items:flex-start;margin-bottom:4px;line-height:18px}
.contact svg{flex:none;margin-top:4px}
.social-row{display:flex;gap:9px;margin-top:2px}
.social-row span{width:20px;height:20px;background:var(--white);border-radius:50%}
.footer-rule{position:absolute;left:73px;top:212px;width:845px;height:1px;background:var(--rule)}
.copyright{position:absolute;left:0;top:229px;width:991px;text-align:center;font-size:9px;color:var(--muted)}
</style>
</head>
<body>

<div class="hero-photo" role="img" aria-label="Photo of a smiling legal team gathered around a laptop in an office"></div>
<div class="nav-bar"></div>
<div class="hero-panel"></div>

<div class="brand">Pollard Law Firm</div>

<nav class="main-nav">
  <a href="#">Home</a><a href="#">About us</a><a href="#">News</a><a href="#">Contact us</a><a href="#">Practice</a>
</nav>
<a class="call-btn" href="#" aria-label="Call">
  <svg width="14" height="14" viewBox="0 0 24 24"><path fill="#fff" d="M6.6 10.8a15.1 15.1 0 0 0 6.6 6.6l2.2-2.2c.3-.3.7-.4 1-.2 1.1.4 2.3.6 3.6.6.6 0 1 .4 1 1V20c0 .6-.4 1-1 1C10.6 21 3 13.4 3 4c0-.6.4-1 1-1h3.5c.6 0 1 .4 1 1 0 1.3.2 2.5.6 3.6.1.3 0 .7-.2 1z"/></svg>
</a>

<header class="hero-text">
  <p class="eyebrow">NEWS &amp; TESTIMONIALS</p>
  <h1 class="hero-title">The Latest<br>from <em>Pollard</em><br>Law Firm</h1>
</header>

<article class="post-card red" style="left:75px">
  <h2 class="post-title">Trucking Company Offers 6 Figure Settlement</h2>
  <p class="post-meta">JULY 1, 2019</p>
</article>
<article class="post-card dark" style="left:357px">
  <h2 class="post-title">DCS Chooses to Dismiss Case</h2>
  <p class="post-meta">MARCH 14, 2019<br>CHILD CUSTODY</p>
</article>
<article class="post-card red" style="left:641px">
  <h2 class="post-title">Pollard Obtains Jury Verdict of 61 x Medical Bills</h2>
  <p class="post-meta">OCTOBER 1, 2018<br>LAW, PERSONAL INJURY</p>
</article>

<article class="feature-post">
  <h2 class="post-title">Insurance Company Pays for Facial Fractures</h2>
  <p class="post-meta">AUGUST 1, 2018 PERSONAL INJURY</p>
</article>

<footer class="site-footer">
  <div class="footer-brand">Pollard Law Firm</div>

  <div class="footer-col" style="left:327px">
    <h3>Quick Links</h3>
    <ul><li>Home</li><li>About us</li><li>News</li><li>Contact us</li><li>Practice</li></ul>
  </div>

  <div class="footer-col contact" style="left:493px">
    <h3>Contact Us</h3>
    <ul>
      <li><svg width="9" height="11" viewBox="0 0 24 30"><path fill="#fff" d="M12 0C5.4 0 0 5.4 0 12c0 9 12 18 12 18s12-9 12-18C24 5.4 18.6 0 12 0zm0 17a5 5 0 1 1 0-10 5 5 0 0 1 0 10z"/></svg><span style="font-size:10px">1480 Maple Ridge Road | Suite 200<br>| Brentwood, TN 37027</span></li>
      <li><svg width="10" height="10" viewBox="0 0 24 24"><path fill="#fff" d="M6.6 10.8a15.1 15.1 0 0 0 6.6 6.6l2.2-2.2c.3-.3.7-.4 1-.2 1.1.4 2.3.6 3.6.6.6 0 1 .4 1 1V20c0 .6-.4 1-1 1C10.6 21 3 13.4 3 4c0-.6.4-1 1-1h3.5c.6 0 1 .4 1 1 0 1.3.2 2.5.6 3.6.1.3 0 .7-.2 1z"/></svg><span style="font-size:10px">Phone: (615) 555-0142</span></li>
      <li><svg width="11" height="9" viewBox="0 0 24 18"><path fill="#fff" d="M0 0h24v2L12 10 0 2zM0 5l12 8 12-8v13H0z"/></svg><span style="font-size:10px">Email: office@pollardlaw-example.com</span></li>
    </ul>
  </div>

  <div class="footer-col" style="left:749px">
    <h3>Social</h3>
    <div class="social-row" aria-label="Social links"><span></span><span></span><span></span><span></span></div>
  </div>

  <div class="footer-rule"></div>
  <p class="copyright">©2021 Pollard Law Firm, PLLC.&nbsp; All Rights Reserved.</p>
</footer>

</body>
</html>
```